Werbetafel für Immobilienverwaltung
Zielgruppe
Wir sind im Kern eine Immobilienverwaltung, daher richten wir uns an Eigentümer/Investoren/Kapitalanleger. Neben der Verwaltung welche auch durch Hausmeisterservice (Grünarbeiten usw.) erweitert werden kann, bieten wir die Gutachtenerstellung sowie den Vertrieb (Maklertätigkeit in Verkauf sowie Vermietung) an.
Ein großer Vorteil ist unsere Digitale Arbeitsweise (noch keine Selbstverständlichkeit in der Branche).
Aufgabenstellung
Ziel ist es, das Unternehmen unaufdringlich jedoch wirksam und informativ auf einer Werbetafel zu präsentieren.
Maße der Tafel, welche sich im ausgangsbereich eines großen Lebensmittelunternehmens befindet, ist B 320cm x H 120cm.
Die Kundschaft läuft in ca. 1m Entfernung an der Tafel vorbei, sie sollte also von nahem nicht zu überrumpelt wirken.
Unser Logo sowie Telefonnummer sollte iwie untergebracht werden.
Gern auch eigene Ideen umsetzen falls Ihr welche habt.

```html
<!DOCTYPE html>
<html lang="de">
<head>
<meta charset="utf-8">
<title>Kaiblick Immobilien – Werbetafel</title>
<link href="https://fonts.googleapis.com/css2?family=Raleway:wght@500;600;800;900&display=swap" rel="stylesheet">
<style>
  :root {
    --frame: #403c3c;
    --paper: #ffffff;
    --brand-red: #9a1d1d;
    --text-grey: #6a6a6a;
    --line-grey: #cfcfcf;
    --photo-glass-a: #f2f2f2;
    --photo-glass-b: #bfc2c4;
    --photo-warm-a: #f2b9a3;
    --photo-warm-b: #c7604a;
    --photo-deep-a: #d98a70;
    --photo-deep-b: #8a2e22;
  }
  * { box-sizing: border-box; margin: 0; padding: 0; }
  html, body { width: 1200px; height: 518px; overflow: hidden; }
  body {
    background: var(--frame);
    font-family: "Raleway", Arial, sans-serif;
    position: relative;
  }
  .billboard {
    position: absolute;
    left: 53px; top: 57px;
    width: 1100px; height: 413px;
    background: var(--paper);
    overflow: hidden;
    border-bottom: 3px solid var(--brand-red);
  }
  .collage { position: absolute; inset: 0; width: 1100px; height: 413px; }

  .brand { position: absolute; left: 38px; top: 70px; width: 354px; }
  .brand-name {
    font-weight: 600; font-size: 34px; color: var(--brand-red);
    display: flex; align-items: center; gap: 10px; line-height: 1;
  }
  .brand-mark { width: 12px; height: 12px; background: var(--brand-red); display: inline-block; }
  .brand-tagline {
    margin-top: 10px; padding-top: 6px; padding-left: 22px;
    border-top: 1px solid var(--line-grey);
    font-size: 11px; font-weight: 500; letter-spacing: 0.7px; color: var(--text-grey);
    white-space: nowrap;
  }

  .headline {
    position: absolute; left: 36px; top: 190px;
    font-weight: 900; font-size: 35px; line-height: 37px; letter-spacing: 0.4px;
    color: var(--brand-red); text-transform: uppercase; white-space: nowrap;
  }

  .contact-pill {
    position: absolute; left: 36px; width: 366px; height: 37px;
    background: var(--brand-red); border-radius: 6px;
    display: flex; align-items: center; color: #fff;
  }
  .contact-pill.phone { top: 303px; }
  .contact-pill.web { top: 349px; }
  .pill-icon {
    width: 42px; height: 100%; display: flex; align-items: center; justify-content: center;
    border-right: 2px solid rgba(255,255,255,0.85);
  }
  .pill-icon svg { width: 18px; height: 18px; fill: #fff; }
  .pill-text { font-weight: 800; white-space: nowrap; }
  .phone .pill-text { padding-left: 30px; font-size: 31px; }
  .web .pill-text { padding-left: 14px; font-size: 25px; }

  .skyline {
    position: absolute; left: 413px; top: 312px; width: 239px; height: 97px;
    background: linear-gradient(to top, rgba(240,240,240,0.7), rgba(250,250,250,0));
  }

  .property-types {
    position: absolute; left: 590px; top: 127px; width: 240px;
    text-align: center; color: #fff; font-weight: 800; font-size: 18px; letter-spacing: 0.3px;
  }
  .property-types li { list-style: none; height: 45px; line-height: 27px; }
</style>
</head>
<body>
  <main class="billboard">
    <svg class="collage" viewBox="65 70 1357 510" preserveAspectRatio="none">
      <defs>
        <linearGradient id="glass" x1="0" y1="0" x2="1" y2="1">
          <stop offset="0" stop-color="var(--photo-glass-a)"/>
          <stop offset="1" stop-color="var(--photo-glass-b)"/>
        </linearGradient>
        <linearGradient id="warm" x1="0" y1="0" x2="1" y2="1">
          <stop offset="0" stop-color="var(--photo-warm-a)"/>
          <stop offset="1" stop-color="var(--photo-warm-b)"/>
        </linearGradient>
        <linearGradient id="deep" x1="0" y1="0" x2="1" y2="1">
          <stop offset="0" stop-color="var(--photo-deep-a)"/>
          <stop offset="1" stop-color="var(--photo-deep-b)"/>
        </linearGradient>
      </defs>
      <polygon role="img" aria-label="Foto: Glasfassade eines Hochhauses von unten" fill="url(#glass)"
               points="560,70 1000,70 772,290 700,215"/>
      <polygon role="img" aria-label="Foto: Einfamilienhaus mit Ziegeldach" fill="url(#warm)"
               points="1005,70 1262,70 1112,278 958,120"/>
      <polygon role="img" aria-label="Foto: moderne Bürofassade mit Fensterreihen" fill="url(#warm)"
               points="1282,70 1422,70 1422,322 1298,456 1130,290"/>
      <polygon fill="var(--brand-red)" points="1422,70 1422,110 1380,70"/>
      <polygon role="img" aria-label="Foto: Wohnanlage mit Balkonen" fill="url(#deep)"
               points="1110,305 1288,480 1385,580 1060,580 955,462"/>
      <polygon fill="var(--brand-red)" points="1422,340 1422,580 1405,580 1302,462"/>
      <polygon fill="#dcdcdc" points="845,580 960,478 1058,580"/>
      <polygon fill="var(--brand-red)" points="940,135 1100,293 940,452 782,293"/>
    </svg>

    <div class="brand">
      <div class="brand-name"><span class="brand-mark"></span>Kaiblick Immobilien</div>
      <div class="brand-tagline">WIR KÜMMERN UNS UM IHR ZUHAUSE</div>
    </div>

    <h1 class="headline">Alle Immobilienservices<br>unter einem Hut</h1>

    <div class="contact-pill phone">
      <span class="pill-icon"><svg viewBox="0 0 24 24"><path d="M6.6 10.8a15.1 15.1 0 0 0 6.6 6.6l2.2-2.2a1 1 0 0 1 1-.25 11.4 11.4 0 0 0 3.6.57 1 1 0 0 1 1 1V20a1 1 0 0 1-1 1A17 17 0 0 1 3 4a1 1 0 0 1 1-1h3.5a1 1 0 0 1 1 1c0 1.25.2 2.45.57 3.57a1 1 0 0 1-.25 1z"/></svg></span>
      <span class="pill-text">0391 480 27 63</span>
    </div>
    <div class="contact-pill web">
      <span class="pill-icon"><svg viewBox="0 0 24 24"><path d="M12 3 2 12h3v8h5v-5h4v5h5v-8h3z"/></svg></span>
      <span class="pill-text">kaiblick-immobilien.de</span>
    </div>

    <div class="skyline" role="img" aria-label="Dezente Strichzeichnung einer Stadtsilhouette"></div>

    <ul class="property-types">
      <li>HAUS</li>
      <li>MISCHNUTZUNG</li>
      <li>WOHNUNG</li>
    </ul>
  </main>
</body>
</html>
```